Banner Ad for Resume Services Website

The add is for this web site: www.BrightCareerPages.net

The site offers 4 different services:

- Resume Writing (by a Certified Professional Resume Writer)
- Resume Posting (posts your resume to 85 job sites)
- Resume Distribution (sends your resume to hundreds of recruiters)
- Resume Online website (created an online resume with a domain name to your name)

Colors to be used are Blue, Yellow, etc... please check the website for inspiration.

Check the web site to learn more.

Target Market(s)

Unemployed, Professionals who want to switch jobs, etc..

Industry/Entity Type

Requirements
Must have
• We definitely one this to be included on the banner:

"Free Resume Samples"

in order to attract clicks.
Nice to have
• Some of the words we suggest to include on the banner are:

"How Good is Your Resume? Ask a Professional !"

Should not have
• No animation !

Do not place the LOGO on the banner as our LOGO might change in the near future. If you already submitted a banner with the LOGO on it, you can replace it with any other graphic that has a Resume/Jobs/BusinessStaff related theme.

```html
<!DOCTYPE html>
<html lang="en">
<head>
<meta charset="utf-8">
<title>BrightCareerPages – Free Resume Samples Banner</title>
<link rel="stylesheet" href="https://fonts.googleapis.com/css2?family=Open+Sans:wght@400;600;700&family=Kalam:wght@400&display=swap">
<style>
  :root {
    --stage: #4f5457;
    --banner-border: #9aa3aa;
    --sky-top: #e9f4fc;
    --sky-bottom: #cde5f6;
    --panel-blue: #0b5aa8;
    --panel-deep: #063f86;
    --panel-rim: #1b3f9a;
    --brand-text: #f3f7fc;
    --brand-dot: #f07a1e;
    --ink-grey: #3c4248;
    --ink-blue: #1467ad;
    --accent-orange: #f26a1b;
    --button-top: #2a86d6;
    --button-bottom: #0a4f98;
    --preview-top: #ffffff;
    --preview-bottom: #e4e6e8;
  }
  * { margin: 0; padding: 0; box-sizing: border-box; }
  html, body {
    width: 1200px;
    height: 900px;
    overflow: hidden;
    background: var(--stage);
  }
  .banner {
    position: absolute;
    left: 54px;
    top: 383px;
    width: 1092px;
    height: 135px;
    overflow: hidden;
    border: 1px solid var(--banner-border);
    background: linear-gradient(180deg, var(--sky-top) 0%, var(--sky-bottom) 70%, #e3f1fb 100%);
    font-family: "Open Sans", Arial, sans-serif;
  }
  .brand-panel {
    position: absolute;
    left: 0;
    top: 0;
    width: 280px;
    height: 135px;
  }
  .brand-dot {
    position: absolute;
    left: 92px;
    top: 22px;
    width: 66px;
    height: 66px;
    border-radius: 50%;
    background: var(--brand-dot);
  }
  .brand-name {
    position: absolute;
    left: 8px;
    top: 98px;
    width: 250px;
    font-size: 13.5px;
    font-weight: 600;
    letter-spacing: 0.8px;
    color: var(--brand-text);
    white-space: nowrap;
  }
  .question {
    position: absolute;
    left: 283px;
    top: 18px;
    font-size: 27px;
    font-weight: 400;
    color: var(--ink-grey);
    white-space: nowrap;
  }
  .offer {
    position: absolute;
    left: 281px;
    top: 50px;
    font-size: 49px;
    font-weight: 400;
    color: var(--ink-blue);
    white-space: nowrap;
    letter-spacing: -0.5px;
  }
  .offer-free {
    font-family: "Kalam", "Comic Sans MS", cursive;
    color: var(--accent-orange);
    font-size: 54px;
    margin-right: 6px;
  }
  .site-preview {
    position: absolute;
    left: 818px;
    top: 6px;
    width: 248px;
    height: 135px;
    border: 1px solid #c9cdd1;
    background: linear-gradient(180deg, var(--preview-top) 0%, var(--preview-bottom) 100%);
  }
  .cta-button {
    position: absolute;
    left: 954px;
    top: 80px;
    width: 126px;
    height: 44px;
    border-radius: 7px;
    border: 1px solid #083f7c;
    background: linear-gradient(180deg, var(--button-top) 0%, var(--button-bottom) 100%);
    color: #ffffff;
    font-size: 20px;
    font-weight: 600;
    line-height: 42px;
    text-align: center;
    box-shadow: 0 2px 4px rgba(0,0,0,0.3);
  }
</style>
</head>
<body>
  <div class="banner">
    <svg class="brand-panel" viewBox="0 0 280 135" aria-hidden="true">
      <defs>
        <linearGradient id="panelFill" x1="0" y1="0" x2="0" y2="1">
          <stop offset="0" stop-color="var(--panel-blue)"/>
          <stop offset="1" stop-color="var(--panel-deep)"/>
        </linearGradient>
      </defs>
      <path d="M0 0 H216 C244 40 260 90 268 135 H0 Z" fill="var(--panel-rim)"/>
      <path d="M0 0 H200 C228 40 246 90 254 135 H0 Z" fill="url(#panelFill)"/>
    </svg>
    <span class="brand-dot" aria-hidden="true"></span>
    <p class="brand-name">www.BrightCareerPages.net</p>

    <p class="question">How Good is Your Resume?</p>
    <p class="offer"><span class="offer-free">Free</span>Resume Samples</p>

    <div class="site-preview" role="img" aria-label="Preview of an online resume web page with a profile photo and sections"></div>
    <div class="cta-button">Get Now</div>
  </div>
</body>
</html>
```